Powerpoint template for Meadowlark Crossing

I need a powerpoint template for my business that would also work for Google slides.
I intermittently deliver training to people and I want a nice powerpoint template, that could also work in google docs to help make production easier and more seamless for me. I also sometimes product reports and analyses that are best done in powerpoint or Google slides. I need a title page, Title and content page, section heading page and any other pages that someone normally has!

Target Market(s)

Leaders and managers in medium to large companies. I provide training and coaching services to senior staff who have got 'stuck' and want help to find their way forward.

Font styles to use
Sans Serif

Requirements
Must have
• Colours and fonts to fit with logo please.
• Must include the logo and company name.
Nice to have
• a picture for the front?

```html
<!DOCTYPE html>
<html lang="en">
<head>
<meta charset="utf-8">
<title>Meadowlark Crossing – Slide Template</title>
<link rel="stylesheet" href="https://fonts.googleapis.com/css2?family=Open+Sans:wght@400;600;700&display=swap">
<style>
:root{
  --stage:#2a2a2a;
  --purple:#4d2f99;
  --purple-dark:#3c2380;
  --teal:#2eae8c;
  --teal-light:#5cc5a6;
  --teal-dark:#1f8a6c;
  --ink:#555;
  --muted:#8a8a8a;
  --rule:#e6e6e6;
  --footer:#efefef;
  --white:#fff;
  --bar-a:#3a5db8;
  --bar-b:#1f3278;
}
*{box-sizing:border-box;margin:0;padding:0}
html,body{width:1200px;height:2687px;overflow:hidden;background:var(--stage);font-family:"Open Sans",Arial,sans-serif}
.board{position:relative;width:1200px;height:2687px}
.slide{position:absolute;width:562px;height:307px;background:var(--white);overflow:hidden}
.col-l{left:14px}.col-r{left:609px}
.photo{position:absolute}
.head{position:absolute;left:26px;top:22px;border-left:3px solid var(--purple);padding-left:10px;color:var(--purple)}
.head .sub{font-size:13px;line-height:16px}
.head .ttl{font-size:17px;font-weight:700;line-height:20px}
.head.light{border-color:var(--white);color:var(--white)}
.body{position:absolute;font-size:8px;line-height:13px;color:var(--ink)}
.body p+p{margin-top:10px}
.body.light{color:var(--white)}
.brand-mini{position:absolute;right:12px;top:9px;width:56px;text-align:center;color:var(--purple);font-size:7px;font-weight:700;line-height:8px;text-transform:uppercase}
.brand-mini .dot{display:block;width:14px;height:14px;border-radius:50%;background:var(--teal);margin:0 auto 3px}
.brand-big{position:absolute;text-align:center;color:var(--purple);font-weight:700;text-transform:uppercase}
.brand-big .dot{display:block;border-radius:50%;background:var(--teal);margin:0 auto}
.footer{position:absolute;left:0;right:0;bottom:0;height:16px;background:var(--footer);font-size:7.5px;line-height:16px;color:#444;padding-left:8px}
.page-no{position:absolute;right:6px;bottom:3px;width:20px;height:20px;border-radius:50%;background:var(--teal);color:var(--white);font-size:7.5px;font-weight:700;text-align:center;line-height:20px}
.vline{position:absolute;width:1px;background:var(--teal-light)}
.feature{position:absolute;width:140px;text-align:center}
.feature svg{display:block;margin:0 auto 8px}
.feature h4{font-size:9.5px;font-weight:700;margin-bottom:4px}
.feature p{font-size:7.5px;line-height:11.5px}
.big-title{position:absolute;color:var(--white);font-weight:700;border-left:3px solid var(--purple);padding-left:12px}
.table{position:absolute;left:12px;top:72px;width:538px;border-collapse:collapse;font-size:7.5px;color:var(--ink)}
.table th{background:var(--teal);color:var(--white);text-align:left;font-size:9px;font-weight:700;height:18px;padding:0 10px}
.table td{height:38px;padding:0 10px;border-bottom:4px solid var(--white);background:#f4f4f4;line-height:11px}
.table td.key{width:110px;font-weight:600;color:#444}
.table tr:nth-child(even) td{background:#ebebeb}
</style>
</head>
<body>
<main class="board">

  <section class="slide col-l slide-contact" style="top:18px;background:var(--purple)">
    <div style="position:absolute;left:376px;top:0;width:156px;height:307px;background:var(--white)"></div>
    <div class="brand-big" style="left:382px;top:110px;width:144px;font-size:15px;line-height:18px"><span class="dot" style="width:46px;height:46px;margin-bottom:10px"></span>Meadowlark Crossing</div>
    <div class="big-title" style="left:20px;top:68px;font-size:22px;line-height:28px;border-color:var(--white)">Contact Me</div>
    <div class="body light" style="left:50px;top:124px;font-size:13.5px;line-height:20px">
      <p>Email Id :<br>hello@meadowlarkcrossing.com</p>
      <p style="margin-top:14px">Website :<br>www.meadowlarkcrossing.com</p>
    </div>
  </section>

  <section class="slide col-r slide-thanks" style="top:18px;background:var(--teal)">
    <div style="position:absolute;left:384px;top:0;width:148px;height:307px;background:var(--white)"></div>
    <div class="brand-big" style="left:388px;top:110px;width:140px;font-size:15px;line-height:18px"><span class="dot" style="width:46px;height:46px;margin-bottom:10px"></span>Meadowlark Crossing</div>
    <div class="big-title" style="left:36px;top:140px;font-size:22px;line-height:34px">Thank you for your time</div>
  </section>

  <section class="slide col-l slide-features-band" style="top:371px">
    <div class="head"><div class="sub">Subtitle Here</div><div class="ttl">Paragraph Title</div></div>
    <div class="brand-mini"><span class="dot"></span>Meadowlark Crossing</div>
    <div style="position:absolute;left:0;top:112px;width:562px;height:195px;background:var(--teal)"></div>
    <div class="feature" style="left:46px;top:128px;color:var(--white)">
      <svg width="30" height="36" viewBox="0 0 30 36"><rect x="7" y="2" width="16" height="30" rx="3" fill="none" stroke="#fff" stroke-width="2.5"/><circle cx="15" cy="27" r="1.8" fill="#fff"/></svg>
      <h4>Icon Text Here</h4><p>Lorem Ipsum is simply dummy text of the printing and typesetting industry. Lorem Ipsum has been the industry's standard dummy text ever since the 1500s, when an unknown printer took a galley of type and scrambled</p>
    </div>
    <div class="feature" style="left:211px;top:128px;color:var(--white)">
      <svg width="40" height="36" viewBox="0 0 40 36"><circle cx="20" cy="9" r="6" fill="#fff"/><circle cx="8" cy="13" r="4.5" fill="#fff"/><circle cx="32" cy="13" r="4.5" fill="#fff"/><path d="M11 32v-8a9 9 0 0 1 18 0v8z M1 32v-6a7 7 0 0 1 9-6v12z M39 32v-6a7 7 0 0 0-9-6v12z" fill="#fff"/></svg>
      <h4>Icon Text Here</h4><p>Lorem Ipsum is simply dummy text of the printing and typesetting industry. Lorem Ipsum has been the industry's standard dummy text ever since the 1500s, when an unknown printer took a galley of type and scrambled</p>
    </div>
    <div class="feature" style="left:376px;top:128px;color:var(--white)">
      <svg width="40" height="36" viewBox="0 0 40 36"><g fill="#fff"><rect x="6" y="24" width="4" height="10"/><rect x="13" y="19" width="4" height="15"/><rect x="20" y="14" width="4" height="20"/><rect x="27" y="9" width="4" height="25"/></g><path d="M4 18 L14 10 L22 13 L34 3" stroke="#fff" stroke-width="2" fill="none"/></svg>
      <h4>Icon Text Here</h4><p>Lorem Ipsum is simply dummy text of the printing and typesetting industry. Lorem Ipsum has been the industry's standard dummy text ever since the 1500s, when an unknown printer took a galley of type and scrambled</p>
    </div>
  </section>

  <section class="slide col-r slide-section-divider" style="top:371px">
    <div class="photo" role="img" aria-label="Young green plant sprouting from dark soil against a soft green background" style="inset:0;background:radial-gradient(circle at 75% 45%,#b6d35a 0%,#6f9a2c 35%,#3f6118 70%,#2c3a12 100%)"></div>
    <div class="big-title" style="left:20px;top:130px;font-size:19px;line-height:24px;border-color:var(--purple)">Sectione Divider Title Here<div style="font-size:13px;font-weight:400;line-height:17px">Subtitle Here</div></div>
  </section>

  <section class="slide col-l slide-title" style="top:709px">
    <div class="photo" role="img" aria-label="Green valley landscape with a teal colour overlay" style="inset:0;background:linear-gradient(160deg,#6fc2ae 0%,#2fa487 45%,#1b8068 100%)"></div>
    <svg style="position:absolute;inset:0" width="562" height="307" viewBox="0 0 562 307">
      <polygon points="200,0 562,0 562,307 442,307" fill="#fff"/>
      <polygon points="462,0 562,0 562,93" fill="var(--purple)"/>
      <line x1="34" y1="0" x2="34" y2="307" stroke="#fff" stroke-opacity=".5"/>
    </svg>
    <div class="brand-big" style="left:362px;top:90px;width:190px;font-size:20px;line-height:24px"><span class="dot" style="width:54px;height:54px;margin-bottom:10px"></span>Meadowlark Crossing</div>
    <div class="big-title" style="left:34px;top:200px;font-size:19px;line-height:24px;border-color:var(--purple)">Project Title Here<div style="font-size:13px;font-weight:400;line-height:17px">Subtitle Here</div></div>
  </section>

  <section class="slide col-r slide-text" style="top:709px">
    <div class="head"><div class="sub">Subtitle Here</div><div class="ttl">Paragraph Title</div></div>
    <div class="brand-mini"><span class="dot"></span>Meadowlark Crossing</div>
    <div class="body" style="left:26px;top:84px;width:510px">
      <p>Lorem Ipsum is simply dummy text of the printing and typesetting industry. Lorem Ipsum has been the industry's standard dummy text ever since the 1500s, when an unknown printer took a galley of type and scrambled it to make a type specimen book. It has survived not only five centuries, but also the leap into electronic typesetting, remaining essentially unchanged. It was popularised in the 1960s with the release of Marlowe Type sheets containing Lorem Ipsum passages, and more recently with desktop publishing software like Quillset Publisher including versions of Lorem Ipsum. Lorem Ipsum is simply dummy text of the printing and typesetting industry.</p>
      <p>Lorem Ipsum has been the industry's standard dummy text ever since the 1500s, when an unknown printer took a galley of type and scrambled it to make a type specimen book. It has survived not only five centuries, but also the leap into electronic typesetting, remaining essentially unchanged.</p>
      <p>It was popularised in the 1960s with the release of Marlowe Type sheets containing Lorem Ipsum passages, and more recently with desktop publishing software like Quillset Publisher including versions of Lorem Ipsum.</p>
    </div>
    <div class="footer">Copyright text here</div><div class="page-no">01</div>
  </section>

  <section class="slide col-l slide-brand-text" style="top:1030px">
    <div class="brand-big" style="left:30px;top:88px;width:180px;font-size:20px;line-height:24px"><span class="dot" style="width:60px;height:60px;margin-bottom:12px"></span>Meadowlark Crossing</div>
    <div class="vline" style="left:247px;top:0;height:291px"></div>
    <div class="head" style="left:247px;top:86px"><div class="sub">Subtitle Here</div><div class="ttl">Paragraph Title</div></div>
    <div class="brand-mini"><span class="dot"></span>Meadowlark Crossing</div>
    <div class="body" style="left:262px;top:132px;width:280px">Lorem Ipsum is simply dummy text of the printing and typesetting industry. Lorem Ipsum has been the industry's standard dummy text ever since the 1500s, when an unknown printer took a galley of type and scrambled it to make a type specimen book. It has survived not only five centuries, but also the leap into electronic typesetting, remaining essentially unchanged. It was popularised in the 1960s with the release of Marlowe Type sheets containing Lorem Ipsum passages, and more recently with desktop publishing software like Quillset Publisher including versions of Lorem Ipsum.</div>
    <div class="footer">Copyright text here</div><div class="page-no">01</div>
  </section>

  <section class="slide col-r slide-two-col" style="top:1030px">
    <div class="head"><div class="sub">Subtitle Here</div><div class="ttl">Paragraph Title</div></div>
    <div class="brand-mini"><span class="dot"></span>Meadowlark Crossing</div>
    <div class="body" style="left:26px;top:76px;width:240px">Lorem Ipsum is simply dummy text of the printing and typesetting industry. Lorem Ipsum has been the industry's standard dummy text ever since the 1500s, when an unknown printer took a galley of type and scrambled it to make a type specimen book. It has survived not only five centuries, but also the leap into electronic typesetting, remaining essentially unchanged. It was popularised in the 1960s with the release of Marlowe Type sheets containing Lorem Ipsum passages, and more recently with desktop publishing software like Quillset Publisher including versions of Lorem Ipsum. Lorem Ipsum is simply dummy text of the printing and typesetting industry. Lorem Ipsum has been the industry's</div>
    <div class="body" style="left:300px;top:76px;width:240px">Lorem Ipsum is simply dummy text of the printing and typesetting industry. Lorem Ipsum has been the industry's standard dummy text ever since the 1500s, when an unknown printer took a galley of type and scrambled it to make a type specimen book. It has survived not only five centuries, but also the leap into electronic typesetting, remaining essentially unchanged. It was popularised in the 1960s with the release of Marlowe Type sheets containing Lorem Ipsum passages, and more recently with desktop publishing software like Quillset Publisher including versions of Lorem Ipsum. Lorem Ipsum is simply dummy text of the printing and typesetting industry. Lorem Ipsum has been the industry's</div>
    <div class="footer">Copyright text here</div><div class="page-no">01</div>
  </section>

  <section class="slide col-l slide-photo-text" style="top:1356px">
    <div class="photo" role="img" aria-label="Small green seedling growing in soil" style="left:0;top:0;width:216px;height:291px;background:radial-gradient(circle at 60% 40%,#d7ef8c 0%,#8fc23d 40%,#4f7d1c 75%,#3a2e1c 100%)"></div>
    <div class="vline" style="left:247px;top:0;height:291px"></div>
    <div class="head" style="left:247px;top:82px"><div class="sub">Subtitle Here</div><div class="ttl">Paragraph Title</div></div>
    <div class="brand-mini"><span class="dot"></span>Meadowlark Crossing</div>
    <div class="body" style="left:262px;top:128px;width:280px">Lorem Ipsum is simply dummy text of the printing and typesetting industry. Lorem Ipsum has been the industry's standard dummy text ever since the 1500s, when an unknown printer took a galley of type and scrambled it to make a type specimen book. It has survived not only five centuries, but also the leap into electronic typesetting, remaining essentially unchanged. It was popularised in the 1960s with the release of Marlowe Type sheets containing Lorem Ipsum passages, and more recently with desktop publishing software like Quillset Publisher including versions of Lorem Ipsum.</div>
    <div class="footer">Copyright text here</div><div class="page-no">01</div>
  </section>

  <section class="slide col-r slide-features" style="top:1356px">
    <div class="head"><div class="sub">Subtitle Here</div><div class="ttl">Paragraph Title</div></div>
    <div class="brand-mini"><span class="dot"></span>Meadowlark Crossing</div>
    <div class="feature" style="left:40px;top:104px;color:var(--ink)">
      <svg width="30" height="36" viewBox="0 0 30 36"><rect x="7" y="2" width="16" height="30" rx="3" fill="none" stroke="var(--purple)" stroke-width="3"/><circle cx="15" cy="27" r="1.8" fill="var(--purple)"/></svg>
      <h4 style="color:var(--purple)">Icon Text Here</h4><p>Lorem Ipsum is simply dummy text of the printing and typesetting industry. Lorem Ipsum has been the industry's standard dummy text ever since the 1500s, when an unknown printer took a galley of type and scrambled</p>
    </div>
    <div class="feature" style="left:211px;top:104px;color:var(--ink)">
      <svg width="40" height="36" viewBox="0 0 40 36"><g fill="var(--teal)"><circle cx="20" cy="9" r="6"/><circle cx="8" cy="13" r="4.5"/><circle cx="32" cy="13" r="4.5"/><path d="M11 32v-8a9 9 0 0 1 18 0v8z M1 32v-6a7 7 0 0 1 9-6v12z M39 32v-6a7 7 0 0 0-9-6v12z"/></g></svg>
      <h4 style="color:var(--teal)">Icon Text Here</h4><p>Lorem Ipsum is simply dummy text of the printing and typesetting industry. Lorem Ipsum has been the industry's standard dummy text ever since the 1500s, when an unknown printer took a galley of type and scrambled</p>
    </div>
    <div class="feature" style="left:382px;top:104px;color:var(--ink)">
      <svg width="40" height="36" viewBox="0 0 40 36"><g fill="var(--purple)"><rect x="6" y="24" width="4" height="10"/><rect x="13" y="19" width="4" height="15"/><rect x="20" y="14" width="4" height="20"/><rect x="27" y="9" width="4" height="25"/></g><path d="M4 18 L14 10 L22 13 L34 3" stroke="var(--purple)" stroke-width="2" fill="none"/></svg>
      <h4 style="color:var(--purple)">Icon Text Here</h4><p>Lorem Ipsum is simply dummy text of the printing and typesetting industry. Lorem Ipsum has been the industry's standard dummy text ever since the 1500s, when an unknown printer took a galley of type and scrambled</p>
    </div>
    <div class="footer">Copyright text here</div><div class="page-no">01</div>
  </section>

  <section class="slide col-l slide-text-photos" style="top:1707px">
    <div class="vline" style="left:190px;top:0;height:291px"></div>
    <div class="head" style="left:20px;top:80px"><div class="sub">Subtitle Here</div><div class="ttl">Paragraph Title</div></div>
    <div class="brand-mini"><span class="dot"></span>Meadowlark Crossing</div>
    <div class="body" style="left:205px;top:74px;width:300px">Lorem Ipsum is simply dummy text of the printing and typesetting industry. Lorem Ipsum has been the industry's standard dummy text ever since the 1500s, when an unknown printer took a galley of type and scrambled it to make a type specimen book. It has survived not only five centuries, but also the leap into electronic a type specimen book.</div>
    <div class="photo" role="img" aria-label="Close-up of a green seedling" style="left:206px;top:170px;width:92px;height:121px;background:radial-gradient(circle at 40% 40%,#cde88a 0%,#86b53a 45%,#3f6a1a 100%)"></div>
    <div class="photo" role="img" aria-label="Sunset over rocky hills" style="left:301px;top:170px;width:261px;height:121px;background:linear-gradient(180deg,#c9a57a 0%,#e8b46a 35%,#8a6a4a 65%,#4a3a2a 100%)"></div>
    <div class="footer">Copyright text here</div><div class="page-no">01</div>
  </section>

  <section class="slide col-r slide-panel-photo" style="top:1707px">
    <div style="position:absolute;left:0;top:0;width:246px;height:291px;background:var(--purple)"></div>
    <div class="head light" style="left:20px;top:46px"><div class="sub">Subtitle Here</div><div class="ttl">Paragraph Title</div></div>
    <div class="body light" style="left:34px;top:92px;width:196px">Lorem Ipsum is simply dummy text of the printing and typesetting industry. Lorem Ipsum has been the industry's standard dummy text ever since the 1500s, when an unknown printer took a galley of type and scrambled it to make a type specimen book. It has survived not only five centuries, but also the leap into electronic a type specimen book.</div>
    <div class="photo" role="img" aria-label="Sunlit forest path with green grass" style="left:246px;top:0;width:316px;height:291px;background:linear-gradient(180deg,#2e4a14 0%,#5f8a24 40%,#8fc23a 70%,#4f7a1c 100%)"></div>
    <div class="footer">Copyright text here</div><div class="page-no">01</div>
  </section>

  <section class="slide col-l slide-table" style="top:2033px">
    <div class="head" style="top:16px"><div class="sub">Subtitle Here</div><div class="ttl">Paragraph Title</div></div>
    <div class="brand-mini"><span class="dot"></span>Meadowlark Crossing</div>
    <table class="table">
      <thead><tr><th>SECTION</th><th>MAIN TITLE HERE</th></tr></thead>
      <tbody>
        <tr><td class="key">ICON -1</td><td>Liquorice chups chups applicake apple pie cupcake brownie bear claw cake gingerbread cotton candy. Bear claw croissant apple pie. Croissant cake sweet puff oreo. Liquorice chups chups applicake apple pie</td></tr>
        <tr><td class="key">ICON -1</td><td>Liquorice chups chups applicake apple pie cupcake brownie bear claw cake gingerbread cotton candy. Bear claw croissant apple pie. Croissant cake sweet puff oreo. Liquorice chups chups applicake apple pie</td></tr>
        <tr><td class="key">ICON -1</td><td>Liquorice chups chups applicake apple pie cupcake brownie bear claw cake gingerbread cotton candy. Bear claw croissant apple pie. Croissant cake sweet puff oreo. Liquorice chups chups applicake apple pie</td></tr>
        <tr><td class="key">ICON -1</td><td>Liquorice chups chups applicake apple pie cupcake brownie bear claw cake gingerbread cotton candy. Bear claw croissant apple pie. Croissant cake sweet puff oreo. Liquorice chups chups applicake apple pie</td></tr>
        <tr><td class="key">ICON -1</td><td>Liquorice chups chups applicake apple pie cupcake brownie bear claw cake gingerbread cotton candy. Bear claw croissant apple pie. Croissant cake sweet puff oreo. Liquorice chups chups applicake apple pie</td></tr>
      </tbody>
    </table>
    <div class="footer">Copyright text here</div><div class="page-no">01</div>
  </section>

  <section class="slide col-r slide-photo-box" style="top:2033px">
    <div class="photo" role="img" aria-label="Wide mountain valley under a blue sky with clouds" style="left:0;top:0;width:562px;height:291px;background:linear-gradient(180deg,#8fb4d8 0%,#c9dbea 35%,#6f8a5a 55%,#3f5a2e 80%,#2c3e22 100%)"></div>
    <div style="position:absolute;left:310px;top:0;width:202px;height:212px;background:var(--purple)"></div>
    <div class="head light" style="left:322px;top:20px"><div class="sub">Subtitle Here</div><div class="ttl">Paragraph Title</div></div>
    <div class="body light" style="left:335px;top:66px;width:168px">Lorem Ipsum is simply dummy text of the printing and typesetting industry. Lorem Ipsum has been the industry's standard dummy text ever since the 1500s, when an unknown printer took a galley of type and scrambled it to make a type specimen book. It has survived not only five centuries, but also the leap into electronic a type specimen book.</div>
    <div class="footer">Copyright text here</div><div class="page-no">01</div>
  </section>

  <section class="slide col-l slide-graph-peaks" style="top:2373px">
    <div class="head" style="top:16px"><div class="sub">Subtitle Here</div><div class="ttl">Graphs Title</div></div>
    <div class="brand-mini"><span class="dot"></span>Meadowlark Crossing</div>
    <svg style="position:absolute;left:0;top:0" width="562" height="307" viewBox="0 0 562 307" aria-label="Peak chart">
      <g fill="var(--teal-light)" fill-opacity=".85">
        <path d="M0 300 Q50 290 70 230 Q90 290 150 300z"/>
        <path d="M90 300 Q140 285 155 175 Q170 285 220 300z"/>
        <path d="M150 300 Q205 280 220 90 Q235 280 290 300z"/>
        <path d="M240 300 Q275 290 290 200 Q305 290 340 300z"/>
        <path d="M290 300 Q355 280 370 130 Q385 280 450 300z"/>
        <path d="M380 300 Q420 292 435 245 Q450 292 490 300z"/>
        <path d="M440 300 Q490 290 510 220 Q530 290 562 300z"/>
      </g>
      <g fill="var(--teal-dark)" fill-opacity=".6">
        <path d="M200 300 Q240 290 260 215 Q280 290 320 300z"/>
        <path d="M320 300 Q360 292 380 240 Q400 292 440 300z"/>
      </g>
      <g stroke="var(--teal)" stroke-width="1"><line x1="70" y1="216" x2="70" y2="228"/><line x1="155" y1="162" x2="155" y2="174"/><line x1="220" y1="76" x2="220" y2="88"/><line x1="290" y1="186" x2="290" y2="198"/><line x1="370" y1="116" x2="370" y2="128"/><line x1="435" y1="231" x2="435" y2="243"/><line x1="510" y1="206" x2="510" y2="218"/></g>
      <g fill="var(--teal)">
        <circle cx="70" cy="202" r="14"/><circle cx="155" cy="148" r="14"/><circle cx="220" cy="62" r="14"/>
        <circle cx="290" cy="172" r="14" fill="var(--teal-dark)"/><circle cx="370" cy="102" r="14"/>
        <circle cx="435" cy="217" r="14"/><circle cx="510" cy="192" r="14"/>
      </g>
      <g fill="#fff" stroke="none">
        <rect x="64" y="199" width="12" height="6" rx="3"/>
        <rect x="150" y="143" width="10" height="10" rx="1"/>
        <path d="M214 66v-7h3l3-5h2v5h4v7z"/>
        <path d="M285 167h10v6l-5 4l-5-4z"/>
        <path d="M364 104l6-7l6 7v5h-12z"/>
        <path d="M435 210v12M430 218q5 5 10 0" stroke="#fff" stroke-width="1.8" fill="none"/>
        <rect x="503" y="186" width="14" height="9" rx="1"/>
      </g>
    </svg>
  </section>

  <section class="slide col-r slide-graph-bars" style="top:2373px">
    <div class="head" style="top:16px"><div class="sub">Subtitle Here</div><div class="ttl">Graphs Title</div></div>
    <div class="brand-mini"><span class="dot"></span>Meadowlark Crossing</div>
    <svg style="position:absolute;left:0;top:0" width="562" height="307" viewBox="0 0 562 307" aria-label="Three bar charts" font-family="Open Sans, Arial, sans-serif" font-size="7" fill="#888">
      <g id="chart-1" transform="translate(40,80)">
        <g stroke="var(--rule)"><line x1="0" y1="0" x2="120" y2="0"/><line x1="0" y1="40" x2="120" y2="40"/><line x1="0" y1="80" x2="120" y2="80"/><line x1="0" y1="120" x2="120" y2="120"/><line x1="0" y1="160" x2="120" y2="160"/><line x1="0" y1="200" x2="120" y2="200" stroke="#bbb"/></g>
        <g text-anchor="end"><text x="-4" y="3">5</text><text x="-4" y="43">4</text><text x="-4" y="83">3</text><text x="-4" y="123">2</text><text x="-4" y="163">1</text><text x="-4" y="203">0</text></g>
        <rect x="6" y="160" width="26" height="40" fill="var(--bar-a)"/><rect x="32" y="140" width="26" height="60" fill="var(--bar-b)"/><rect x="58" y="120" width="26" height="80" fill="var(--bar-a)"/><rect x="84" y="80" width="26" height="120" fill="var(--bar-b)"/>
      </g>
      <g id="chart-2" transform="translate(222,80)">
        <g stroke="var(--rule)"><line x1="0" y1="0" x2="120" y2="0"/><line x1="0" y1="40" x2="120" y2="40"/><line x1="0" y1="80" x2="120" y2="80"/><line x1="0" y1="120" x2="120" y2="120"/><line x1="0" y1="160" x2="120" y2="160"/><line x1="0" y1="200" x2="120" y2="200" stroke="#bbb"/></g>
        <g text-anchor="end"><text x="-4" y="3">5</text><text x="-4" y="43">4</text><text x="-4" y="83">3</text><text x="-4" y="123">2</text><text x="-4" y="163">1</text><text x="-4" y="203">0</text></g>
        <rect x="6" y="188" width="26" height="12" fill="var(--bar-a)"/><rect x="32" y="152" width="26" height="48" fill="var(--bar-b)"/><rect x="58" y="160" width="26" height="40" fill="var(--bar-a)"/><rect x="84" y="136" width="26" height="64" fill="var(--bar-b)"/>
      </g>
      <g id="chart-3" transform="translate(404,80)">
        <g stroke="var(--rule)"><line x1="0" y1="0" x2="120" y2="0"/><line x1="0" y1="40" x2="120" y2="40"/><line x1="0" y1="80" x2="120" y2="80"/><line x1="0" y1="120" x2="120" y2="120"/><line x1="0" y1="160" x2="120" y2="160"/><line x1="0" y1="200" x2="120" y2="200" stroke="#bbb"/></g>
        <g text-anchor="end"><text x="-4" y="3">5</text><text x="-4" y="43">4</text><text x="-4" y="83">3</text><text x="-4" y="123">2</text><text x="-4" y="163">1</text><text x="-4" y="203">0</text></g>
        <rect x="6" y="0" width="26" height="200" fill="var(--bar-a)"/><rect x="32" y="96" width="26" height="104" fill="var(--bar-b)"/><rect x="58" y="60" width="26" height="140" fill="var(--bar-a)"/><rect x="84" y="128" width="26" height="72" fill="var(--bar-b)"/>
      </g>
    </svg>
  </section>

</main>
</body>
</html>
```